Tolvik's Trim spring flyers

I am needing a flyer design for my lawn mowing business. my services are mowing, edging, weed eating, vacuuming with strong attention to detail. residential and commercial. Mowing average $35 and Spring clean up average $79. Looking for fun, professional and colorful to grab the eye and stand out. rough sizing of 10"x4"

Target Market(s)

people needing lawn care and spring clean up

Font styles to use
Serif

Colors

Designer to choose colors to be used in the design.

Requirements
Must have
• Services listed and pricing listed
• please add licensed and insured
• 417-555-0183
• dorsebrian7@fernmail.test
• FREE ESTIMATES

```html
<!DOCTYPE html>
<html lang="en">
<head>
<meta charset="utf-8">
<title>Tolvik's Trim – Spring Flyer</title>
<link rel="stylesheet" href="https://fonts.googleapis.com/css2?family=Oswald:wght@500;600;700&family=Montserrat:wght@600;700&display=swap">
<style>
  :root {
    --blue: #1f7acb;
    --blue-dark: #155f9f;
    --navy: #1e3450;
    --ink: #222a33;
    --grey-light: #f4f5f6;
    --grey-mid: #c9cdd1;
    --white: #ffffff;
    --lawn: #5e9a3a;
  }
  * { margin: 0; padding: 0; box-sizing: border-box; }
  html, body { width: 1200px; height: 2293px; overflow: hidden; background: var(--white); }
  .flyer {
    position: relative; width: 1200px; height: 2293px; overflow: hidden;
    background: linear-gradient(180deg, var(--white) 34%, #e9ebed 55%, var(--grey-mid) 80%, var(--white) 86%);
    font-family: "Montserrat", sans-serif; color: var(--ink);
  }
  .hero-photo {
    position: absolute; left: 0; top: 0; width: 1200px; height: 800px;
    background: linear-gradient(180deg, #8a8f92 0%, #b7b3a8 30%, #6d7f5a 55%, var(--lawn) 75%, #7fb34a 100%);
  }
  .hero-wave { position: absolute; left: 0; top: 560px; width: 1200px; height: 340px; }
  .brand { position: absolute; top: 830px; left: 0; width: 1200px; text-align: center; }
  .brand-dot {
    width: 190px; height: 190px; margin: 0 auto 40px; border-radius: 50%;
    background: var(--navy);
  }
  .brand-name {
    font-family: "Montserrat", sans-serif; font-weight: 700; font-size: 96px;
    color: var(--navy); letter-spacing: 1px;
  }
  .market {
    position: absolute; top: 1225px; width: 1200px; text-align: center;
    font-family: "Oswald", sans-serif; font-weight: 600; font-size: 54px; color: var(--ink);
  }
  .services { position: absolute; top: 1340px; left: 70px; width: 1060px; display: flex; justify-content: space-between; }
  .service { width: 230px; text-align: center; }
  .service-badge { width: 210px; height: 210px; margin: 0 auto; display: block; }
  .service-label {
    margin-top: 20px; font-family: "Oswald", sans-serif; font-weight: 600;
    font-size: 36px; line-height: 1.15; color: var(--ink);
  }
  .prices { position: absolute; top: 1690px; left: 55px; width: 1090px; display: flex; justify-content: space-between; }
  .price-card {
    width: 520px; height: 215px; background: var(--white);
    border: 4px dashed #9aa3ab; outline: 10px solid var(--white);
    box-shadow: 0 6px 14px rgba(0,0,0,.25);
    display: flex; align-items: center; justify-content: center; gap: 24px;
  }
  .price-amount { font-family: "Oswald", sans-serif; font-weight: 700; font-size: 150px; color: var(--blue); line-height: 1; }
  .price-item { font-family: "Oswald", sans-serif; font-weight: 600; font-size: 54px; line-height: 1.05; color: var(--ink); }
  .footer-wave { position: absolute; left: 0; top: 1920px; width: 1200px; height: 140px; }
  .licensed {
    position: absolute; top: 2060px; width: 1200px; text-align: center;
    font-weight: 700; font-size: 50px; color: var(--ink);
  }
  .estimate-bar {
    position: absolute; top: 2148px; left: 115px; width: 970px; height: 84px;
    border-radius: 42px; background: var(--blue);
    display: flex; align-items: center; justify-content: center; gap: 26px;
    font-weight: 700; font-size: 46px; color: var(--white);
  }
  .phone-icon { width: 52px; height: 52px; }
  .email {
    position: absolute; top: 2242px; width: 1200px; text-align: center;
    font-weight: 600; font-size: 34px; color: var(--ink);
  }
</style>
</head>
<body>
<main class="flyer">
  <div class="hero-photo" role="img" aria-label="Photo of a grey house entrance with a neatly mowed green lawn and flower beds"></div>
  <svg class="hero-wave" viewBox="0 0 1200 340" preserveAspectRatio="none" aria-hidden="true">
    <path d="M0 60 C 300 320, 800 240, 1200 120 L1200 340 L0 340 Z" fill="var(--white)"/>
    <path d="M0 60 C 300 320, 800 240, 1200 120 L1200 160 C 800 270, 320 330, 0 90 Z" fill="var(--blue)"/>
    <path d="M0 160 C 300 330, 800 270, 1200 170 L1200 340 L0 340 Z" fill="#e6f0fa" opacity=".7"/>
  </svg>

  <header class="brand">
    <div class="brand-dot"></div>
    <h1 class="brand-name">TOLVIK'S TRIM</h1>
  </header>

  <p class="market">RESIDENTIAL &amp; COMMERCIAL</p>

  <section class="services">
    <div class="service">
      <svg class="service-badge" viewBox="0 0 100 100" role="img" aria-label="Lawn mower icon">
        <polygon points="50,4 90,27 90,73 50,96 10,73 10,27" fill="var(--white)" stroke="var(--blue)" stroke-width="4"/>
        <circle cx="50" cy="50" r="26" fill="var(--ink)"/>
      </svg>
      <p class="service-label">LAWN<br>MOWING</p>
    </div>
    <div class="service">
      <svg class="service-badge" viewBox="0 0 100 100" role="img" aria-label="Lawn edger icon">
        <polygon points="50,4 90,27 90,73 50,96 10,73 10,27" fill="var(--white)" stroke="var(--blue)" stroke-width="4"/>
        <circle cx="50" cy="50" r="26" fill="var(--ink)"/>
      </svg>
      <p class="service-label">LAWN<br>EDGING</p>
    </div>
    <div class="service">
      <svg class="service-badge" viewBox="0 0 100 100" role="img" aria-label="Grass tuft icon">
        <polygon points="50,4 90,27 90,73 50,96 10,73 10,27" fill="var(--white)" stroke="var(--blue)" stroke-width="4"/>
        <circle cx="50" cy="50" r="26" fill="var(--ink)"/>
      </svg>
      <p class="service-label">WEED<br>EATING</p>
    </div>
    <div class="service">
      <svg class="service-badge" viewBox="0 0 100 100" role="img" aria-label="Fan icon for lawn vacuuming">
        <polygon points="50,4 90,27 90,73 50,96 10,73 10,27" fill="var(--white)" stroke="var(--blue)" stroke-width="4"/>
        <circle cx="50" cy="50" r="26" fill="var(--ink)"/>
      </svg>
      <p class="service-label">LAWN<br>VACUUMING</p>
    </div>
  </section>

  <section class="prices">
    <div class="price-card">
      <span class="price-amount">$35</span>
      <span class="price-item">LAWN<br>MOWING</span>
    </div>
    <div class="price-card">
      <span class="price-amount">$79</span>
      <span class="price-item">SPRING<br>CLEAN UP</span>
    </div>
  </section>

  <svg class="footer-wave" viewBox="0 0 1200 140" preserveAspectRatio="none" aria-hidden="true">
    <path d="M0 140 C 400 130, 900 100, 1200 0 L1200 140 Z" fill="var(--white)"/>
    <path d="M0 140 C 400 130, 900 100, 1200 0 L1200 30 C 900 120, 400 145, 0 140 Z" fill="var(--blue)"/>
  </svg>

  <p class="licensed">Licensed and Insured</p>

  <div class="estimate-bar">
    <span>FREE ESTIMATES</span>
    <svg class="phone-icon" viewBox="0 0 24 24" aria-hidden="true">
      <circle cx="12" cy="12" r="10.5" fill="none" stroke="var(--white)" stroke-width="1.8"/>
      <path d="M8.6 6.8c.4-.3 1-.2 1.2.3l.8 1.8c.2.4.1.8-.2 1.1l-.7.6c.6 1.3 1.6 2.3 2.9 2.9l.6-.7c.3-.3.7-.4 1.1-.2l1.8.8c.5.2.6.8.3 1.2l-.8 1c-.4.5-1.1.7-1.7.5-3.2-1-5.7-3.5-6.7-6.7-.2-.6 0-1.3.5-1.7z" fill="var(--white)"/>
    </svg>
    <span>417-555-0183</span>
  </div>

  <p class="email">dorsebrian7@fernmail.test</p>
</main>
</body>
</html>
```